Tamarack Hearth Partners Business Card

Looking for a new business card layout. We are a real estate firm w/ a logo, old design attached. Must keep the same elements on there, just need a fresh look and possible some foil accents. Looking for a simpler design w/ more modern style.

Target Market(s)

Real Estate clients

Industry/Entity Type

Real Estate Agent

Contact Information for Business Card

see attached

Font styles to use
Sans Serif

Requirements
Must have
• all elements on current biz card
Nice to have
• modern look, simpler than we have!
Should not have
• no serif fonts

```html
<!DOCTYPE html>
<html lang="en">
<head>
<meta charset="utf-8">
<title>Tamarack Hearth Partners – Business Card</title>
<link href="https://fonts.googleapis.com/css2?family=Lato:wght@400;700&family=Montserrat:wght@800&display=swap" rel="stylesheet">
<style>
  :root {
    --page-bg: #d9d9db;
    --card-white: #ffffff;
    --ink: #1e1e1e;
    --blue-light: #8fcdee;
    --blue-mid: #6bb3e3;
    --blue-deep: #3a92d6;
    --photo-ring: #2f86cf;
    --text-on-blue: #ffffff;
  }
  * { box-sizing: border-box; margin: 0; padding: 0; }
  html, body { width: 1200px; height: 900px; overflow: hidden; }
  body {
    background: var(--page-bg);
    font-family: "Lato", sans-serif;
    position: relative;
  }
  .card {
    position: absolute;
    width: 640px;
    height: 366px;
    background: var(--card-white);
    box-shadow: 0 6px 18px rgba(0,0,0,0.18);
    overflow: hidden;
  }
  .card-front { left: 110px; top: 60px; }
  .card-back { left: 450px; top: 474px; }

  .brand-name {
    font-family: "Montserrat", sans-serif;
    font-weight: 800;
    color: var(--ink);
    line-height: 1.05;
    letter-spacing: 0.5px;
  }
  .card-front .brand-name {
    position: absolute;
    left: 0; right: 0; top: 128px;
    text-align: center;
    font-size: 44px;
  }

  .back-shapes { position: absolute; inset: 0; }
  .card-back .brand-name {
    position: absolute;
    left: 32px; top: 120px;
    font-size: 24px;
    width: 300px;
  }
  .agent-photo {
    position: absolute;
    right: 38px; top: 22px;
    width: 176px; height: 176px;
    border-radius: 50%;
    border: 3px solid var(--photo-ring);
    padding: 5px;
    background: var(--card-white);
  }
  .agent-photo-fill {
    width: 100%; height: 100%;
    border-radius: 50%;
    background: radial-gradient(circle at 50% 45%, #f0d9b5 0%, #d8b98a 45%, #b9c7c4 100%);
  }
  .agent-details {
    position: absolute;
    left: 150px; top: 212px;
    color: var(--text-on-blue);
  }
  .agent-name { font-weight: 700; font-size: 20px; line-height: 24px; }
  .agent-title { font-size: 12px; line-height: 15px; margin-bottom: 5px; }
  .contact-list { list-style: none; font-size: 12px; line-height: 16px; }
  .contact-list li { display: flex; align-items: center; gap: 7px; }
  .contact-list svg { width: 12px; height: 12px; flex: none; }
  .contact-list .contact-address { margin-top: 4px; line-height: 15px; align-items: flex-start; }
</style>
</head>
<body>

<section class="card card-front">
  <p class="brand-name">TAMARACK HEARTH<br>PARTNERS</p>
</section>

<section class="card card-back">
  <svg class="back-shapes" viewBox="0 0 640 366" width="640" height="366">
    <defs>
      <linearGradient id="bandGradient" x1="0" y1="1" x2="1" y2="0">
        <stop offset="0" stop-color="var(--blue-mid)"/>
        <stop offset="0.55" stop-color="var(--blue-light)"/>
        <stop offset="1" stop-color="var(--blue-mid)"/>
      </linearGradient>
    </defs>
    <polygon points="150,198 640,198 640,206 142,206" fill="var(--blue-deep)"/>
    <polygon points="0,366 0,330 142,206 640,206 640,366" fill="url(#bandGradient)"/>
  </svg>

  <p class="brand-name">TAMARACK HEARTH<br>PARTNERS</p>

  <div class="agent-photo">
    <div class="agent-photo-fill" role="img" aria-label="Portrait photo of the agent"></div>
  </div>

  <div class="agent-details">
    <p class="agent-name">Dana Wrenfield</p>
    <p class="agent-title">Principal Broker</p>
    <ul class="contact-list">
      <li><svg viewBox="0 0 12 12"><circle cx="6" cy="6" r="5.3" fill="none" stroke="#fff" stroke-width="1"/><path d="M4 3.2 5 4.6 4.5 5.3q.8 1.4 2.2 2.2l.7-.5 1.4 1-.6.9Q5.5 8.7 3.2 4.3z" fill="#fff"/></svg>555.210.4837</li>
      <li><svg viewBox="0 0 12 12"><circle cx="6" cy="6" r="5.3" fill="none" stroke="#fff" stroke-width="1"/><rect x="3.4" y="4.6" width="5.2" height="3.4" rx=".6" fill="#fff"/><path d="M3.2 4.2q2.8-1.6 5.6 0" stroke="#fff" fill="none"/></svg>555.318.6294</li>
      <li><svg viewBox="0 0 12 12"><circle cx="6" cy="6" r="5.3" fill="none" stroke="#fff" stroke-width="1"/><rect x="4.3" y="2.9" width="3.4" height="6.2" rx=".6" fill="none" stroke="#fff"/></svg>dana@hearthkeys.com</li>
      <li><svg viewBox="0 0 12 12"><circle cx="6" cy="6" r="5.3" fill="none" stroke="#fff" stroke-width="1"/><rect x="3.3" y="4" width="5.4" height="4" fill="#fff"/><path d="M3.3 4 6 6.2 8.7 4" stroke="var(--blue-mid)" fill="none" stroke-width=".8"/></svg>tamarackhearth-homes.com</li>
      <li class="contact-address"><svg viewBox="0 0 12 12" style="width:15px;height:15px"><path d="M6 11.5Q1.5 6.8 1.5 4.6a4.5 4.5 0 0 1 9 0Q10.5 6.8 6 11.5z" fill="#fff"/><circle cx="6" cy="4.6" r="1.6" fill="var(--blue-mid)"/></svg><span>48 NW Larch Ave Pinecrest,<br>OR 97000</span></li>
    </ul>
  </div>
</section>

</body>
</html>
```